Folded Business Cards for Guarantee, Layaway & The Fine Print

I am looking for a set of (3) folded business for our guarantee, layaway and fine print policies. I would like the same design for each of these cards, with the exception of the picture, title and verbiage.
The front of each card must include our logo, the title of the card (Our Guarantee, Layaway or The Fine Print,) and a picture of a piece of jewelry. The inside of the card should state our policies. The back of the card should have our logo, address (Bellstone Court #9, Londonderry, NH 03053,) phone # (555-281-0947) email & web address (info@vantorgems.com, www.vantorgems.com) and social media icons (FB, Twitter, Pinterest, Instagram)

The layaway card needs a place for the customer's signature.

I was thinking the orientation of the card should be vertical but if the right design ends up being horizontal, I'm ok with that. I do have concerns about readability and that this may be too much information for a folded business card. So, I am open to either changing the front & back, if need be or going to a different format (standard postcard size. Verbiage may also need to be trimmed down, but I need to know what is possible first.

Our branding colors are espresso brown & coppery orange so please do not stray from this color palette. The font of our logo is joefin. I would like the verbiage of the cards to be in quattrocento sans font. We would like a modern & clean look please.

Attached, please find our logo, policies and jewelry pictures. For picture placement, please do the following: Layaway Card (Quartz & onyx pendant,) The Fine Print Card (Orange Garnet Pendant,) Our Guarantee (triple Green Tourmaline Ring.)

```html
<!DOCTYPE html>
<html lang="en">
<head>
<meta charset="utf-8">
<title>Layaway Card – Inside</title>
<link rel="stylesheet" href="https://fonts.googleapis.com/css2?family=Quattrocento:wght@400;700&display=swap">
<style>
  :root {
    --copper: #c44f00;
    --espresso: #482503;
    --heading-brown: #5a2703;
    --copper-text: #cc6a1e;
    --blush: #e8c1a8;
    --paper: #ffffff;
  }
  * { margin: 0; padding: 0; box-sizing: border-box; }
  html, body {
    width: 1200px;
    height: 900px;
    overflow: hidden;
    background: var(--paper);
  }
  .card {
    position: absolute;
    left: 111px;
    top: 16px;
    width: 978px;
    height: 865px;
    background: var(--copper);
  }
  .card__header {
    position: absolute;
    left: 0; top: 0;
    width: 100%;
    height: 159px;
  }
  .card__title {
    position: absolute;
    left: 91px;
    top: 68px;
    font-family: "Quattrocento", serif;
    font-weight: 400;
    font-size: 34px;
    line-height: 44px;
    color: var(--heading-brown);
  }
  .card__body {
    position: absolute;
    left: 0; top: 159px;
    width: 100%;
    height: 635px;
    background: var(--espresso);
  }
  .policy-column {
    position: absolute;
    top: 165px;
    width: 414px;
    font-family: "Quattrocento", serif;
    font-size: 27px;
    line-height: 34px;
    color: var(--copper-text);
    text-align: justify;
    hyphens: auto;
  }
  .policy-column--left { left: 61px; }
  .policy-column--right { left: 509px; width: 417px; }
  .policy-column p {
    text-indent: 28px;
    margin-bottom: 6px;
  }
  .signature-box {
    position: absolute;
    left: 609px;
    top: 717px;
    width: 369px;
    height: 148px;
    background: var(--blush);
  }
</style>
</head>
<body>
  <main class="card">
    <header class="card__header">
      <h1 class="card__title">Something to<br>Look Forward to...</h1>
    </header>
    <section class="card__body"></section>

    <div class="policy-column policy-column--left">
      <p>Special occasion shopping made easy.</p>
      <p>Take home the jewelry you love after 6 monthly payments or 3 monthly payments for sale merchandise.</p>
      <p>A 20% deposit secures your layaway.</p>
      <p>Interest free.</p>
      <p>No approval process.</p>
      <p>No finance charges or hidden fees.</p>
      <p>A 5% restocking fee will be charged for layaways cancelled after 30 days.</p>
    </div>

    <div class="policy-column policy-column--right">
      <p>If your layaway is cancelled after 90 days, either by your or us, all deposits and payments will be converted to store credit. Restocking fee applies.</p>
      <p>Custom jewelry &amp; special orders placed on layaway require a 50% deposit and are non-cancellable &amp; non-refundable.</p>
      <p>Vantor’s retains right to cancel any layaway, at any time, for late or inconsistent payments. Cancellation fees &amp; policies, as stated above, will apply.</p>
    </div>

    <div class="signature-box" aria-label="Customer signature area"></div>
  </main>
</body>
</html>
```